Business IT Services Billboard to attract local small businesses

We are Brivolux, a premier Managed Service Provider (MSP) specializing in comprehensive IT services and VOIP phone solutions exclusively for businesses. Our goal is to create a dynamic and visually engaging billboard advertisement that not only highlights our cutting-edge IT solutions but also emphasizes our state-of-the-art VOIP phone services. This billboard should communicate our commitment to providing innovative, reliable, and holistic technology solutions.
Target Market(s)
small business
Industry/Entity Type
Information Technology
Colors
Designer to choose colors to be used in the design.
Look and feel
Each slider illustrates characteristics of the customer's brand and the style your logo design should communicate.

```html
<!DOCTYPE html>
<html lang="en">
<head>
<meta charset="UTF-8">
<title>Brivolux – Innovative IT &amp; VOIP Billboard</title>
<link rel="stylesheet" href="https://fonts.googleapis.com/css2?family=Oswald:wght@600;700&display=swap">
<style>
  :root {
    --page-bg: #eef1f5;
    --brand-blue: #1874c4;
    --deep-navy: #061a3f;
    --suit-navy: #0c2a66;
    --city-blue: #1456b8;
    --glow-blue: #49a6ff;
    --white: #ffffff;
    --band-grey: rgba(255, 255, 255, 0.35);
  }
  html, body {
    margin: 0;
    padding: 0;
    width: 1200px;
    height: 1200px;
    overflow: hidden;
    background: var(--page-bg);
  }
  .canvas {
    width: 1200px;
    height: 1200px;
    display: flex;
    align-items: center;
    justify-content: center;
  }
  .billboard {
    position: relative;
    width: 1120px;
    height: 562px;
    overflow: hidden;
    box-shadow: 0 10px 30px rgba(0, 0, 0, 0.18);
  }
  .hero-photo {
    position: absolute;
    inset: 0;
    background:
      radial-gradient(ellipse 30% 55% at 52% 92%, rgba(160, 215, 255, 0.75), rgba(73, 166, 255, 0) 70%),
      radial-gradient(ellipse 28% 40% at 45% 18%, rgba(73, 166, 255, 0.55), rgba(73, 166, 255, 0) 70%),
      radial-gradient(ellipse 26% 75% at 14% 55%, rgba(6, 26, 63, 0.9), rgba(6, 26, 63, 0) 75%),
      linear-gradient(180deg, var(--city-blue) 0%, #1d6fd6 45%, var(--suit-navy) 100%);
  }
  .overlay {
    position: absolute;
    inset: 0;
    width: 100%;
    height: 100%;
  }
  .headline-text {
    font-family: "Oswald", sans-serif;
    font-weight: 700;
    fill: var(--white);
  }
  .brand-name {
    font-family: "Oswald", sans-serif;
    font-weight: 700;
    fill: var(--brand-blue);
    letter-spacing: 40px;
  }
</style>
</head>
<body>
<main class="canvas">
  <div class="billboard">
    <div class="hero-photo" role="img"
         aria-label="Photo: businessman in a navy suit on a phone call, typing on a laptop, in front of a glowing blue night city skyline with a digital world map"></div>

    <svg class="overlay" viewBox="0 0 1076 540" xmlns="http://www.w3.org/2000/svg">
      <g class="headline-tab">
        <path d="M630 0 L1076 0 L1062 172 Q855 205 650 172 Z" fill="var(--brand-blue)"/>
        <path d="M675 188 Q855 222 1025 188" fill="none" stroke="var(--white)" stroke-width="7" stroke-linecap="round"/>
        <text class="headline-text" x="855" y="62" font-size="48" letter-spacing="5" text-anchor="middle">INNOVATIVE</text>
        <text class="headline-text" x="855" y="134" font-size="66" letter-spacing="4" text-anchor="middle">IT &amp; VOIP</text>
        <text class="headline-text" x="855" y="170" font-size="29" font-weight="600" text-anchor="middle">www.brivolux.com</text>
      </g>

      <g class="brand-band">
        <rect x="11" y="236" width="315" height="100" fill="var(--band-grey)"/>
        <rect x="326" y="236" width="750" height="100" fill="var(--white)"/>
        <text class="brand-name" x="706" y="316" font-size="80" text-anchor="middle">BRIVOLUX</text>
      </g>

      <g class="tagline-tab">
        <path d="M695 385 Q858 345 1020 385" fill="none" stroke="var(--white)" stroke-width="8" stroke-linecap="round"/>
        <path d="M652 398 Q858 372 1040 398 L1058 536 L656 536 Z" fill="var(--brand-blue)"/>
        <text class="headline-text" x="857" y="453" font-size="37" text-anchor="middle">SOLUTIONS FOR YOUR</text>
        <text class="headline-text" x="857" y="497" font-size="37" text-anchor="middle">BUSINESS SUCCESS</text>
      </g>
    </svg>
  </div>
</main>
</body>
</html>
```